Heron Renovation Group Postcard Design Project

I'm a General Contractor specializing in luxury residential remodeling.

THIS IS AN EDDM POSTCARD. THE ENTIRE BACK SIDE OF THE CARD WILL BE USED.

I FORGOT TO MENTION THIS IN MY ORIGINAL BRIEF.

Target Market(s)

OLD, rich people so please make sure the fonts are clear and crisp.

Font styles to use
Sans Serif

```html
<!DOCTYPE html>
<html lang="en">
<head>
<meta charset="utf-8">
<title>Heron Renovation Group Postcard</title>
<link rel="stylesheet" href="https://fonts.googleapis.com/css2?family=Cabin:wght@400;500;600;700&family=Cabin+Condensed:wght@600;700&display=swap">
<style>
:root{
  --page-bg:#e6e6e8;
  --card-bg:#ffffff;
  --brand-red:#d9201f;
  --brand-red-dark:#b8161a;
  --ink:#111111;
  --ring-light:#cfe9f8;
  --ring-mid:#9fd4f3;
  --icon-blue:#1aa3e8;
  --pill-start:#5fc3ea;
  --pill-end:#1450a8;
  --photo-wall:#e7a868;
  --photo-cabinet:#efe6d4;
  --photo-floor:#8a4a22;
}
*{box-sizing:border-box;margin:0;padding:0}
html,body{width:1200px;height:1200px;overflow:hidden;background:var(--page-bg);font-family:"Cabin",sans-serif;color:var(--ink)}
.postcard{position:absolute;left:195px;top:0;width:810px;height:1200px;background:var(--card-bg);overflow:hidden}
.hero-photo{position:absolute;left:0;top:0;width:810px;height:448px;
  background:linear-gradient(180deg,#f6efe3 0%,var(--photo-wall) 28%,var(--photo-cabinet) 52%,#d9a06a 72%,var(--photo-floor) 100%)}
.headline-band{position:absolute;left:0;top:448px;width:810px;height:86px;
  background:linear-gradient(180deg,var(--brand-red) 0%,var(--brand-red-dark) 100%);
  color:#fff;text-align:center;font-weight:700;font-size:31px;line-height:39px;padding-top:5px;letter-spacing:.2px}
.headline-rule{position:absolute;left:0;top:534px;width:810px;height:8px;background:var(--ink)}
.values-diagram{position:absolute;left:28px;top:600px;width:400px;height:400px}
.value-label{position:absolute;width:150px;margin-left:-75px;text-align:center;font-weight:700;font-size:15.5px;line-height:19px;color:#1a1a1a}
.core-title{position:absolute;left:128px;top:778px;width:200px;text-align:center;font-weight:700;font-size:29px;line-height:32px}
.brand-block{position:absolute;left:418px;top:690px;width:390px;text-align:center}
.brand-name{display:inline-flex;align-items:center;gap:10px;font-weight:700;font-size:25px;color:var(--brand-red)}
.brand-name .mark{width:16px;height:16px;background:var(--brand-red)}
.services{margin-top:62px;font-size:17.5px;font-weight:500;line-height:22px}
.phone-large{margin-top:26px;font-size:33px;font-weight:700}
.license{margin-top:8px;font-family:"Cabin Condensed",sans-serif;font-weight:700;font-size:19px}
.footer-band{position:absolute;left:0;top:1038px;width:810px;height:117px;background:var(--ink)}
.contact-name{position:absolute;left:62px;top:26px;color:#fff;font-size:38px;font-weight:500;line-height:40px}
.contact-title{position:absolute;left:62px;top:68px;color:#fff;font-size:20px;line-height:24px;letter-spacing:.3px}
.contact-pill{position:absolute;left:377px;top:24px;width:433px;height:78px;border-radius:39px 0 0 39px;
  background:linear-gradient(90deg,var(--pill-start) 0%,var(--pill-end) 70%);color:#fff;font-size:20px;line-height:25px;padding:12px 0 0 46px}
.contact-line{display:flex;align-items:center;gap:10px}
.contact-line svg{width:17px;height:17px}
.footer-accent{position:absolute;left:0;top:1155px;width:810px;height:13px;background:var(--brand-red)}
</style>
</head>
<body>
<main class="postcard">
  <div class="hero-photo" role="img" aria-label="Photo of a bright remodeled kitchen with cream cabinets, an island with stools, pendant lights and a staircase"></div>
  <div class="headline-band">REMODELING LUXURY HOMES &amp; BUILDING<br>LASTING RELATIONSHIPS SINCE 1995</div>
  <div class="headline-rule"></div>

  <svg class="values-diagram" viewBox="0 0 400 400" aria-hidden="true">
    <circle cx="200" cy="200" r="172" fill="none" stroke="var(--ring-light)" stroke-width="2"/>
    <circle cx="200" cy="200" r="158" fill="none" stroke="var(--ring-mid)" stroke-width="3"/>
    <circle cx="200" cy="200" r="140" fill="none" stroke="var(--ring-light)" stroke-width="6"/>
    <circle cx="200" cy="200" r="92" fill="none" stroke="var(--ring-light)" stroke-width="4"/>
    <path d="M120 160 A88 88 0 0 0 250 272" fill="none" stroke="var(--icon-blue)" stroke-width="3"/>
    <path d="M280 160 A88 88 0 0 1 288 200" fill="none" stroke="var(--ring-mid)" stroke-width="5"/>
    <circle cx="200" cy="200" r="78" fill="none" stroke="var(--ring-light)" stroke-width="2"/>
    <g fill="var(--icon-blue)">
      <rect x="175" y="15" width="40" height="40" rx="7"/>
      <rect x="296" y="92" width="40" height="40" rx="7"/>
      <rect x="304" y="240" width="40" height="40" rx="7"/>
      <rect x="176" y="327" width="40" height="40" rx="7"/>
      <rect x="53" y="238" width="40" height="40" rx="7"/>
      <rect x="53" y="93" width="40" height="40" rx="7"/>
    </g>
    <g fill="#fff" stroke="#fff">
      <circle cx="195" cy="27" r="4" stroke="none"/><rect x="189" y="32" width="12" height="7" rx="3" stroke="none"/>
      <circle cx="184" cy="41" r="3" stroke="none"/><circle cx="206" cy="41" r="3" stroke="none"/><rect x="180" y="45" width="30" height="4" rx="2" stroke="none"/>
      <circle cx="316" cy="108" r="6" fill="none" stroke-width="3"/><path d="M302 122 h26" stroke-width="3"/>
      <path d="M312 262 l8 -6 8 6 M314 266 l6 4 10 -8" fill="none" stroke-width="3"/>
      <circle cx="196" cy="347" r="12" fill="none" stroke-width="3"/><circle cx="196" cy="347" r="5" fill="none" stroke-width="3"/>
      <path d="M64 256 l7 7 12 -14" fill="none" stroke-width="4"/>
      <circle cx="73" cy="108" r="8" stroke="none"/><rect x="69" y="117" width="8" height="7" rx="1" stroke="none"/>
    </g>
  </svg>
  <div class="value-label" style="left:225px;top:658px">Educating Our<br>Clients</div>
  <div class="value-label" style="left:101px;top:736px">The Creative<br>Process</div>
  <div class="value-label" style="left:345px;top:736px">Quality<br>Craftsmanship</div>
  <div class="value-label" style="left:101px;top:885px">Integrity</div>
  <div class="value-label" style="left:351px;top:884px">World Class<br>Customer Service</div>
  <div class="value-label" style="left:224px;top:967px">Having Fun</div>
  <div class="core-title">CORE<br>VALUES</div>

  <section class="brand-block">
    <div class="brand-name"><span class="mark"></span>Heron Renovation Group</div>
    <p class="services">All Phases of Residential Remodeling<br>Partial &amp; Large Scale Renovations<br>Complimentary Design Services</p>
    <p class="phone-large">480-555-0172</p>
    <p class="license">Licensed / Bonded &nbsp;/ Insured #418365</p>
  </section>

  <footer class="footer-band">
    <div class="contact-name">Daniel Hale</div>
    <div class="contact-title">General Contractor</div>
    <div class="contact-pill">
      <div class="contact-line">
        <svg viewBox="0 0 20 20" aria-hidden="true"><circle cx="10" cy="10" r="8" fill="none" stroke="#fff" stroke-width="2"/><path d="M2 10h16M10 2c-4 4-4 12 0 16M10 2c4 4 4 12 0 16" fill="none" stroke="#fff" stroke-width="1.5"/></svg>
        <span>www.HeronRenovationGroup.com</span>
      </div>
      <div class="contact-line">
        <svg viewBox="0 0 20 20" aria-hidden="true"><path d="M5 2l3 4-2 2c1 3 3 5 6 6l2-2 4 3-2 3C9 18 2 11 2 4z" fill="#fff"/></svg>
        <span>480-555-0172</span>
      </div>
    </div>
  </footer>
  <div class="footer-accent"></div>
</main>
</body>
</html>
```